TBrenwick Business Cards & Letterhead

I have a logo but need a design for some new business cards. We are a Design-Build Firm that specializes in the design and construction of commercial projects.
the cards need to be professional. no cartoon stuff.
i would like to have the cards in AI format so I can update the card as needed. Logo is provided.
Our Address is: 4718 Fenmoor Ct. Larkfield, Oregon 97318

```html
<!DOCTYPE html>
<html lang="en">
<head>
<meta charset="utf-8">
<title>TBrenwick Business Cards</title>
<link href="https://fonts.googleapis.com/css2?family=Montserrat:wght@400;500;700;800&display=swap" rel="stylesheet">
<style>
  :root {
    --page-bg: #3a3a3a;
    --card-white: #ffffff;
    --card-black: #1b1b1b;
    --brand-blue: #0a6aae;
    --brand-blue-light: #1380c8;
    --ink: #1e1e1e;
    --band-dark: #151515;
  }
  * { margin: 0; padding: 0; box-sizing: border-box; }
  html, body { width: 1200px; height: 1200px; overflow: hidden; }
  body {
    background: var(--page-bg);
    font-family: "Montserrat", sans-serif;
    position: relative;
  }
  .card {
    position: absolute;
    left: 250px;
    width: 700px;
    height: 400px;
    border-radius: 30px;
    overflow: hidden;
    box-shadow: 0 18px 40px rgba(0,0,0,0.45);
  }
  .card-front { top: 150px; background: var(--card-white); }
  .card-back { top: 650px; background: var(--card-black); }

  .front-brand {
    position: absolute;
    right: 70px;
    top: 70px;
    font-weight: 800;
    font-size: 40px;
    letter-spacing: 1px;
    color: var(--brand-blue);
  }

  .contact-block {
    position: absolute;
    left: 60px;
    top: 190px;
  }
  .identity {
    border-left: 6px solid var(--brand-blue);
    padding-left: 10px;
    margin-bottom: 14px;
  }
  .full-name {
    font-weight: 700;
    font-size: 34px;
    line-height: 1;
    color: var(--brand-blue);
  }
  .position {
    font-weight: 500;
    font-size: 17px;
    letter-spacing: 1px;
    color: var(--ink);
    margin-top: 2px;
  }
  .contact-list { list-style: none; padding-left: 22px; }
  .contact-list li {
    display: flex;
    align-items: flex-start;
    gap: 12px;
    font-size: 17px;
    line-height: 1.25;
    color: var(--ink);
    margin-bottom: 2px;
  }
  .contact-list svg { width: 18px; height: 18px; flex: none; margin-top: 2px; fill: var(--brand-blue); }

  .bottom-band { position: absolute; left: 0; bottom: 0; width: 700px; height: 26px; }

  .back-brand {
    position: absolute;
    inset: 0;
    display: flex;
    align-items: center;
    justify-content: center;
    gap: 18px;
  }
  .back-brand .mark-square {
    width: 48px;
    height: 48px;
    background: var(--brand-blue);
  }
  .back-brand .brand-name {
    font-weight: 800;
    font-size: 66px;
    letter-spacing: 1px;
    color: #ffffff;
  }
</style>
</head>
<body>
  <section class="card card-front">
    <div class="front-brand">TBRENWICK</div>

    <div class="contact-block">
      <div class="identity">
        <div class="full-name">FULL NAME</div>
        <div class="position">POSITION</div>
      </div>
      <ul class="contact-list">
        <li>
          <svg viewBox="0 0 24 24"><path d="M6.6 10.8a15.1 15.1 0 0 0 6.6 6.6l2.2-2.2c.3-.3.7-.4 1-.2 1.1.4 2.3.6 3.6.6.6 0 1 .4 1 1V20c0 .6-.4 1-1 1A17 17 0 0 1 3 4c0-.6.4-1 1-1h3.5c.6 0 1 .4 1 1 0 1.3.2 2.5.6 3.6.1.3 0 .7-.2 1z"/></svg>
          <span>(000) 000 0000</span>
        </li>
        <li>
          <svg viewBox="0 0 24 24"><path d="M2 5h20v14H2zM3.5 6.5 12 13l8.5-6.5z" fill-rule="evenodd"/></svg>
          <span>email@company.com</span>
        </li>
        <li>
          <svg viewBox="0 0 24 24"><path d="M12 2a7 7 0 0 0-7 7c0 5.2 7 13 7 13s7-7.8 7-13a7 7 0 0 0-7-7zm0 9.5A2.5 2.5 0 1 1 12 6.5a2.5 2.5 0 0 1 0 5z"/></svg>
          <span>4718 Fenmoor Ct. Larkfield<br>Oregon 97318</span>
        </li>
      </ul>
    </div>

    <svg class="bottom-band" viewBox="0 0 700 26" preserveAspectRatio="none" aria-hidden="true">
      <defs>
        <linearGradient id="bandBlue" x1="0" x2="1">
          <stop offset="0" stop-color="#0a5f9e"/>
          <stop offset="1" stop-color="#1380c8"/>
        </linearGradient>
      </defs>
      <polygon points="0,10 430,0 438,26 0,26" fill="url(#bandBlue)"/>
      <polygon points="448,0 700,0 700,26 456,26" fill="#151515"/>
    </svg>
  </section>

  <section class="card card-back">
    <div class="back-brand">
      <span class="mark-square"></span>
      <span class="brand-name">TBRENWICK</span>
    </div>
  </section>
</body>
</html>
```